Residential Construction Business - Site Signage

I need a design made for a site fence banner. We have a logo and branding so the design would need to be aligned with this. It would need to be made to specific size ratio so that it can be sent to the maker for production.
ratio : 4600 wide x 1700 high
The design should feature our website and also the slogan
"STAY PUT, RE-THINK"

Target Market(s)

potential clients

Industry/Entity Type

construction

Font styles to use
Other font styles liked:
• to match branding

Colors
0054AA
0677BA
7BADD7
CADEEF
E8F1F8

Requirements
Must have
• www.velmbuild.com.au Majority of the sign is our brand logo
Nice to have
• Majority of the sign is our brand logo
Should not have
• colors and themes that arent brand relevant

```html
<!DOCTYPE html>
<html lang="en">
<head>
<meta charset="utf-8">
<title>Velm Build – Site Banner</title>
<link href="https://fonts.googleapis.com/css2?family=Montserrat:wght@500;600&display=swap" rel="stylesheet">
<style>
  :root {
    --navy: #023a5c;
    --paper: #f3f3f5;
  }
  html, body {
    margin: 0;
    padding: 0;
    overflow: hidden;
    background: var(--paper);
  }
  .banner {
    position: relative;
    width: 1200px;
    height: 444px;
    overflow: hidden;
    background: var(--paper);
    font-family: "Montserrat", Arial, sans-serif;
    color: var(--navy);
  }
  .chevron-band {
    position: absolute;
    inset: 0;
    width: 1200px;
    height: 444px;
  }
  .brand-name {
    position: absolute;
    left: 332px;
    top: 197px;
    margin: 0;
    font-size: 46px;
    font-weight: 500;
    letter-spacing: 0.3em;
    line-height: 1;
    white-space: nowrap;
  }
  .divider {
    position: absolute;
    left: 774px;
    top: 145px;
    width: 2px;
    height: 150px;
    background: var(--navy);
  }
  .slogan {
    position: absolute;
    left: 819px;
    top: 154px;
    margin: 0;
    font-size: 28px;
    font-weight: 600;
    letter-spacing: 0.34em;
    line-height: 37px;
    white-space: nowrap;
  }
  .website {
    position: absolute;
    left: 819px;
    top: 267px;
    margin: 0;
    font-size: 17px;
    font-weight: 500;
    letter-spacing: 0.16em;
    line-height: 1;
    white-space: nowrap;
  }
</style>
</head>
<body>
  <main class="banner">
    <svg class="chevron-band" viewBox="0 0 1200 444" aria-hidden="true">
      <path d="M0 0 H495 L315.5 196.7 Q296 220 316.4 246 L512 444 H0 Z" fill="var(--navy)"/>
    </svg>

    <h1 class="brand-name">VELMBUILD</h1>

    <div class="divider"></div>

    <p class="slogan">STAY PUT,<br>RE-THINK</p>

    <p class="website">VELMBUILD.COM.AU</p>
  </main>
</body>
</html>
```